Website design for an Online pastry shop

Website Name : www.lanternandplum.com

Description of the website and its target audience
We are a premium pastry company producing delicious cakes, macarons, cookies, gelato, and other sweet dessert. Our differentiation is that our products are freshly produced with premium quality imported ingredients and one bite into our products set us apart from other bakery shop. We online retail online so as to provide high quality products at a affordable cost. Our products has received raving reviews by many food enthusiast even the hard to please ones. The products contain more natural ingredients and we do not add preservatives. The return rates for our pastry is almost 80%. You only need to try once to be return customers. Our greatest challenge is getting customer to take the first bite. We are so sure of our products that we are going to give people free food tasting.

We are based in China but all our products are developed by award winning chefs from 5 stars hotel. The target customer is woman 16 to 40+ in china. Working class ladies and demand high quality products. A modern, sophisticated and minimalist website

This is a competitive market and image is crucial for such a food ‘conscious ’ orientated customer. They want to feel that they are buying from a reliable company that take great effort to ensure food cleaniness and safety yet affordable price. We make almost 98% of sub ingredients ourselves and we make it by hand.

Style/theme ideas for the web page design
I am looking for a elegant a little rustic, handmade feel yet sophisticated design - one that is easy to the eye yet functional and easy for the user to navigate through. Good play of fonts to give let it feel unique and customised. Black and white is our corporate colours. However, we do not want black background as it does not tease the taste bud. All our colours should come from our products. Customers should be very close to our products. They eat with their eyes first. Black and white is just accent.

Inspirational and competitors websites
http://www.47torte.com/ ( Key competitor )
I like the simple, clean look. The products are the key focus
https://www.pleemo.com/
clean, fresh and different. Attractive with purpose. Feminine
http://quillandbobbin.com/
this has a great layout - lots of information and nicely presented. Very sweet and feminine
http://www.storehavenrow.com/
product features is the focus
http://www.odettevulmers.com/store/
fun, feminine, rustic

Number of pages needed : 6 ( Uncoded PSD design only )
Page descriptions
Home Page - This page will show what makes our products stand out from the competitors and provide an introduction of who we are.
2nd page : Product catalogue
3nd page: Detail Product page with pictures and descriptions. Select products size and add to cart....
4rd page: Brand Story with pictures and descriptions.
5th page Contact Us : Here they can contact or schedule an appointment for free product tasting
6th page : Check out page

Target Market(s)

Female, Asian, Working Class, Office

Industry/Entity Type

Shop

Number of Pages Required

5+ page

Font styles to use
Other font styles liked:
• See packaging

Requirements
Must have
• Please see the project wire frame file " main page.png " or file number 70

```html
<!DOCTYPE html>
<html lang="en">
<head>
<meta charset="utf-8">
<title>Lantern &amp; Plum — Premium Pastry</title>
<link rel="stylesheet" href="https://fonts.googleapis.com/css2?family=Raleway:wght@400;600;700&family=Lato:ital,wght@0,400;0,700;1,400&family=Roboto+Condensed:wght@400;700&display=swap">
<style>
:root{
  --brown:#8a6a4e;
  --brown-dark:#3b2a1f;
  --accent:#a0764f;
  --ink:#333;
  --paper:#f6f6f5;
  --band:#ececec;
  --footer:#2f2f2f;
  --footer-line:#444;
  --star:#e0642a;
  --star-off:#aaa;
}
*{box-sizing:border-box;margin:0;padding:0}
html,body{width:691px;height:1200px;overflow:hidden}
body{font-family:"Lato",sans-serif;color:var(--ink);background:var(--paper);position:relative}
.abs{position:absolute}

/* header */
.topbar{left:0;top:0;width:691px;height:23px;background:var(--brown);border-top:2px solid #3a3a3a;border-bottom:1px dashed #c9b39e;color:#fff;font-size:7px}
.topbar .contact{position:absolute;right:98px;top:6px;display:flex;gap:10px}
.topbar .contact span{display:flex;align-items:center;gap:3px}
.navbar{left:0;top:23px;width:691px;height:47px;background:#f2f2f2}
.logo{left:99px;top:2px;width:99px;height:72px;background:#ececec;border-radius:0 0 3px 3px;box-shadow:0 1px 3px rgba(0,0,0,.3);display:flex;flex-direction:column;align-items:center;justify-content:flex-end;padding-bottom:8px;z-index:5}
.logo .mark{width:20px;height:20px;border-radius:50%;background:var(--brown-dark);margin-bottom:10px}
.logo .name{font-family:"Raleway",sans-serif;font-weight:600;font-size:12px;color:#222}
.nav{left:215px;top:44px;display:flex;font-family:"Roboto Condensed",sans-serif;font-size:8px;color:#222}
.nav span{padding:0 13px;border-left:1px solid #bbb;line-height:9px}
.nav span:first-child{border:0;padding-left:0;color:var(--brown)}
.cart{left:538px;top:42px;font-size:7px;color:var(--brown);display:flex;align-items:center;gap:4px}

/* hero */
.hero{left:0;top:70px;width:691px;height:332px;background:radial-gradient(ellipse at 35% 40%,#f4efe6 0 25%,#dccbb2 45%,#8a7562 75%,#5a4a3d 100%)}
.hero-caption{left:99px;top:270px;width:307px;height:43px;background:rgba(40,34,30,.72);border-left:2px solid #fff;color:#fff;font-family:"Raleway",sans-serif;font-size:15px;line-height:18px;padding:3px 8px}
.hero-caption b{font-weight:700}
.buy{left:99px;top:325px;width:81px;height:18px;background:var(--brown-dark);border:1px solid #c9a98a;border-radius:2px;color:#fff;font-size:9px;font-weight:700;display:flex;align-items:center;justify-content:center}

/* shared */
.section-title{left:0;width:691px;font-family:"Raleway",sans-serif;font-weight:400;font-size:17px;color:#333;text-align:center}
.section-title em{font-style:normal;font-weight:700;color:var(--accent)}
.intro{left:0;width:691px;font-size:6.6px;font-style:italic;color:#555;text-align:center}

/* about */
.about{left:0;top:402px;width:691px;height:140px}
.about .rule{position:absolute;left:233px;top:49px;width:225px;height:1px;background:#ccc}
.about .dot{position:absolute;left:342px;top:46px;width:6px;height:6px;border-radius:50%;background:#999}
.about p{position:absolute;left:140px;top:70px;width:411px;text-align:center;font-size:7.3px;line-height:12px;color:#444}
.about .more{position:absolute;left:0;width:691px;top:113px;text-align:center;font-size:7px;font-weight:700;color:#222}

/* products */
.products{left:0;top:542px;width:691px;height:300px;background:var(--band);border-bottom:1px dashed #bbb}
.pager{left:329px;top:46px;display:flex;gap:2px}
.pager span{width:11px;height:10px;background:#666;display:flex;align-items:center;justify-content:center}
.card{top:82px;width:150px;height:192px;background:#fff;border:1px solid #ddd;border-radius:2px}
.card .photo{height:138px}
.card .title{font-size:8px;font-weight:400;color:#333;margin:6px 0 0 6px}
.stars{margin:3px 0 0 6px;padding-bottom:3px;width:130px;border-bottom:1px dotted #ccc;font-size:11px;line-height:11px;letter-spacing:1px;color:var(--star-off)}
.stars b{font-weight:400;color:var(--star)}
.price{font-size:8.5px;color:#333;margin:4px 0 0 6px}
.actions{position:absolute;left:0;top:114px;width:148px;height:24px;background:rgba(20,16,14,.88);display:flex;color:#fff;font-size:7px}
.actions .add{width:73px;display:flex;align-items:center;gap:4px;padding-left:7px;border-right:1px solid #555}
.actions .icon{width:28px;display:flex;align-items:center;justify-content:center;border-right:1px solid #555}

/* categories */
.categories{left:0;top:842px;width:691px;height:200px}
.categories .section-title{font-weight:700;color:#222}
.tile{top:72px;width:119px;height:79px;border:1px solid #333;border-radius:2px;overflow:hidden}
.tile .fill{height:100%}
.tile .corner{position:absolute;right:0;bottom:0;border-left:14px solid transparent;border-bottom:14px solid #555}
.label{top:163px;width:119px;text-align:center;font-family:"Raleway",sans-serif;font-size:13px;color:#333}
.chev{top:96px}

/* footer */
.footer{left:0;top:1042px;width:691px;height:134px;background:var(--footer);color:#ddd}
.fcol{top:22px}
.fcol h4{font-size:8.5px;font-weight:700;color:#fff;padding-bottom:6px;border-bottom:1px solid var(--footer-line);margin-bottom:8px}
.links{list-style:none;font-size:6.6px;line-height:14px}
.links li::before{content:"› ";color:#aaa}
.fcol p{font-size:6.6px;line-height:10.5px}
.vline{top:24px;width:1px;height:100px;background:var(--footer-line)}
.subscribe{display:flex;margin-top:22px;height:18px}
.subscribe .field{width:90px;background:#fff;color:#555;font-size:6.6px;display:flex;align-items:center;gap:4px;padding-left:5px}
.subscribe .btn{width:55px;background:var(--accent);color:#fff;font-size:6.6px;font-weight:700;display:flex;align-items:center;justify-content:center}
.social{list-style:none}
.social li{display:flex;align-items:center;gap:8px;font-size:5.6px;letter-spacing:.4px;height:18px}
.social li i{width:8px;height:8px;border-radius:50%;background:#ddd;display:block}
.copy{left:0;top:1176px;width:691px;height:24px;background:var(--footer);border-top:1px solid #3b3b3b;color:#aaa;font-size:6.2px;text-align:center;line-height:24px;letter-spacing:.3px}
</style>
</head>
<body>

<header>
  <div class="abs topbar">
    <div class="contact">
      <span><svg width="7" height="7" viewBox="0 0 10 10"><path d="M2 1l2 2-1 1.5c.8 1.5 1.8 2.5 3.5 3.5L8 6l2 2-1.5 1.8C4.5 9.5.5 5.5.2 1.8z" fill="#fff"/></svg>1234567890</span>
      <span><svg width="8" height="6" viewBox="0 0 10 7"><rect width="10" height="7" fill="#fff"/><path d="M0 0l5 4 5-4" stroke="#8a6a4e" fill="none"/></svg>info@lanternplum.com</span>
    </div>
  </div>
  <div class="abs navbar"></div>
  <div class="abs logo"><span class="mark"></span><span class="name">Lantern &amp; Plum</span></div>
  <nav class="abs nav">
    <span>Home</span><span>About Us</span><span>Cake List</span><span>Brand Story</span><span>Contact Us</span>
  </nav>
  <div class="abs cart">
    <svg width="10" height="12" viewBox="0 0 10 12"><rect x="1" y="3" width="8" height="8.5" fill="none" stroke="#555"/><path d="M3 3V2a2 2 0 0 1 4 0v1" fill="none" stroke="#555"/></svg>
    CAET: $0.00
  </div>
</header>

<section class="abs hero" role="img" aria-label="Photo collage of a cream-topped cheesecake and a mango mousse cake on a table"></section>
<div class="abs hero-caption">Our products are developed by<br>Award winning chefs from <b>5 Stars hotels.</b></div>
<div class="abs buy">BUY NOW !</div>

<section class="abs about">
  <h2 class="abs section-title" style="top:22px">About <em>Lantern &amp; Plum</em></h2>
  <span class="rule"></span><span class="dot"></span>
  <p>Lorem ipsum dolor sit amet, consectetuer adipiscing elit, sed diam nonummy nibh euismod tincidunt ut laoreet dolore magna aliquam erat volutpat. Ut wisi enim ad minim veniam, quis nostrud exerci tation ullamcorper suscipit lobortis nisl ut aliquip ex ea commodo consequat. Duis autem vel eum iriure dolor in hendrerit in vulputate velit esse molestie.</p>
  <div class="more">Read More »</div>
</section>

<section class="abs products">
  <h2 class="abs section-title" style="top:22px">Our <em>Products</em></h2>
  <div class="abs pager">
    <span><svg width="6" height="6" viewBox="0 0 6 6"><path d="M4 0L1 3l3 3" stroke="#fff" fill="none" stroke-width="1.4"/></svg></span>
    <span><svg width="6" height="6" viewBox="0 0 6 6"><path d="M2 0l3 3-3 3" stroke="#fff" fill="none" stroke-width="1.4"/></svg></span>
  </div>
  <p class="abs intro" style="top:63px">Lorem ipsum dolor sit amet, consectetuer adipiscing elit, sed diam nonummy nibh euismod tincidunt ut laoreet dolore magna aliquam.</p>

  <article class="abs card" style="left:99px">
    <div class="photo" role="img" aria-label="Photo of dark chocolate curls" style="background:linear-gradient(150deg,#2a1a14,#5a3424 50%,#1e120d)"></div>
    <div class="title" style="margin-left:20px">Lorem ipsum dolor sit amet</div>
    <div class="stars"><b>★★</b>★★★</div>
    <div class="price">$ 312.99</div>
  </article>

  <article class="abs card" style="left:271px">
    <div class="photo" role="img" aria-label="Photo of a chocolate cream cake slice with chocolate shavings" style="background:linear-gradient(180deg,#5b4434 0,#2b1a12 35%,#3a2418 60%,#f1e6cf 75%,#a07448 100%)"></div>
    <div class="actions">
      <span class="add"><svg width="8" height="7" viewBox="0 0 8 7"><path d="M0 0h1.5l1 4h4.5L8 1H2" fill="none" stroke="#fff"/><circle cx="3" cy="6" r=".8" fill="#fff"/><circle cx="6" cy="6" r=".8" fill="#fff"/></svg>Add to Card</span>
      <span class="icon"><svg width="8" height="6" viewBox="0 0 8 6"><path d="M1 3V1h5M5 0l1.5 1L5 2M7 3v2H2M3 4L1.5 5 3 6" fill="none" stroke="#fff" stroke-width=".9"/></svg></span>
      <span class="icon" style="border:0;flex:1"><svg width="8" height="7" viewBox="0 0 8 7"><path d="M4 7L.5 3.5A2 2 0 0 1 4 1a2 2 0 0 1 3.5 2.5z" fill="#fff"/></svg></span>
    </div>
    <div class="title">Lorem ipsum dolor sit amet</div>
    <div class="stars"><b>★★★★</b>★</div>
    <div class="price">$ 912.99</div>
  </article>

  <article class="abs card" style="left:442px">
    <div class="photo" role="img" aria-label="Photo of a cherry-topped cheesecake" style="background:linear-gradient(180deg,#d9ccbc 0,#8c1d2a 30%,#b2283a 55%,#f2e6c8 75%,#e8d8b4 100%)"></div>
    <div class="title">Lorem ipsum dolor sit amet</div>
    <div class="stars"><b>★★★★</b>★</div>
    <div class="price">$ 912.99</div>
  </article>
</section>

<section class="abs categories">
  <h2 class="abs section-title" style="top:27px">Categories</h2>
  <p class="abs intro" style="top:54px">Lorem ipsum dolor sit amet, consectetuer adipiscing elit, sed diam nonummy nibh euismod tincidunt ut laoreet dolore magna aliquam.</p>
  <svg class="abs chev" style="left:78px" width="8" height="14" viewBox="0 0 8 14"><path d="M7 1L1 7l6 6" fill="none" stroke="#bbb" stroke-width="2"/></svg>
  <svg class="abs chev" style="left:603px" width="8" height="14" viewBox="0 0 8 14"><path d="M1 1l6 6-6 6" fill="none" stroke="#bbb" stroke-width="2"/></svg>

  <div class="abs tile" style="left:99px" role="img" aria-label="Photo of a caramel macaron"><div class="fill" style="background:radial-gradient(ellipse at 50% 55%,#d48a4a 0 30%,#f4efe9 55%,#fff)"></div><span class="corner"></span></div>
  <div class="abs tile" style="left:223px" role="img" aria-label="Photo of colourful macaron cookies"><div class="fill" style="background:linear-gradient(135deg,#f5c23a,#ef6aa7 45%,#6fd2c4 75%,#e8398a)"></div><span class="corner"></span></div>
  <div class="abs tile" style="left:348px" role="img" aria-label="Photo of a chocolate cake topped with berries"><div class="fill" style="background:radial-gradient(ellipse at 50% 55%,#5a2a1c 0 35%,#9c2b22 50%,#2a1410 80%)"></div><span class="corner"></span></div>
  <div class="abs tile" style="left:473px" role="img" aria-label="Photo of a meringue-topped pie"><div class="fill" style="background:radial-gradient(ellipse at 50% 65%,#fbfaf7 0 30%,#c79c68 48%,#b9a48c 75%)"></div><span class="corner"></span></div>

  <div class="abs label" style="left:99px">Macarons</div>
  <div class="abs label" style="left:223px">Cookies</div>
  <div class="abs label" style="left:348px">Cakes</div>
  <div class="abs label" style="left:466px">Gelato</div>
</section>

<footer class="abs footer">
  <div class="abs fcol" style="left:100px;width:72px">
    <h4>Quick Links</h4>
    <ul class="links"><li>Home</li><li>About Us</li><li>Cake List</li><li>Brand Story</li><li>Contact</li></ul>
  </div>
  <span class="abs vline" style="left:182px"></span>
  <div class="abs fcol" style="left:203px;width:114px">
    <h4>Contact Detail</h4>
    <p><b>Lanternplum</b><br>Lorem ipsum dolor sitak amet,<br>conse adipiscing elit, euismod poor.</p>
    <p style="margin-top:6px">☏ &nbsp;+123 456 7890</p>
    <p style="margin-top:3px">✉ &nbsp;info@lanternplum.com</p>
  </div>
  <span class="abs vline" style="left:335px"></span>
  <div class="abs fcol" style="left:356px;width:143px">
    <h4>Newsletter Signup</h4>
    <p>Get the latest updates<br>by entering your<br>email address</p>
    <svg class="abs" style="left:84px;top:24px" width="38" height="30" viewBox="0 0 38 30"><polygon points="0,0 38,14 14,18" fill="#ddd"/><polygon points="14,18 18,30 22,17" fill="#aaa"/></svg>
    <div class="subscribe"><span class="field">✉ Enter your email here</span><span class="btn">SUBSCRIBE</span></div>
  </div>
  <div class="abs fcol" style="left:538px;width:60px">
    <h4>Follow Us</h4>
    <ul class="social">
      <li><i></i>FRIENDPAGE</li>
      <li><i></i>CHIRPLINE</li>
      <li><i></i>FRIENDPAGE</li>
      <li><i></i>RSS FEED</li>
    </ul>
  </div>
</footer>
<div class="abs copy">COPYRIGHT © 2015 LANTERNPLUM. ALL RIGHTS RESERVED</div>

</body>
</html>
```